VTM letterhead

We need the Letterhead and a page 2 which will be a simpler page - less header space for the design. Use the design you just created for the Business card. Be sure Page 2 allows for a full page of content.

Industry/Entity Type

Business

```html
<!DOCTYPE html>
<html lang="en">
<head>
<meta charset="utf-8">
<title>VTM Tech Group — Letterhead</title>
<link rel="stylesheet" href="https://fonts.googleapis.com/css2?family=Lato:wght@400;700;900&family=Arimo:wght@400;700&display=swap">
<style>
  :root {
    --backdrop: #ebebeb;
    --paper: #ffffff;
    --brand-red: #c8323b;
    --brand-black: #111111;
    --ink: #1d1d1d;
    --signature-tone: #dcdcdc;
  }
  * { margin: 0; padding: 0; box-sizing: border-box; }
  html, body { width: 1200px; height: 799px; overflow: hidden; }
  body { background: var(--backdrop); position: relative; font-family: "Arimo", Arial, sans-serif; color: var(--ink); }

  .sheet {
    position: absolute; top: 82px; width: 462px; height: 645px;
    background: var(--paper); overflow: hidden;
    box-shadow: 0 2px 6px rgba(0,0,0,0.12);
  }
  .sheet--cover { left: 88px; }
  .sheet--letter { left: 663px; }

  .top-band { position: absolute; left: 0; top: 0; width: 100%; }
  .top-band__red { height: 32px; background: var(--brand-red); }
  .top-band__black { height: 14px; background: var(--brand-black); }

  .footer-wave { position: absolute; left: 0; bottom: 0; width: 462px; height: 72px; display: block; }

  .wordmark { font-family: "Lato", sans-serif; font-weight: 900; color: var(--brand-black); text-transform: uppercase; }
  .wordmark--large { position: absolute; left: 0; width: 100%; top: 262px; text-align: center; line-height: 1; }
  .wordmark--large .wordmark__name { display: block; font-size: 104px; letter-spacing: 3px; }
  .wordmark--large .wordmark__sub { display: block; font-size: 24px; letter-spacing: 1px; margin-top: 6px; }

  .wordmark--small { position: absolute; left: 56px; top: 22px; line-height: 1; }
  .wordmark--small .wordmark__name { display: block; font-size: 30px; letter-spacing: 1px; }
  .wordmark--small .wordmark__sub { display: block; font-size: 8.5px; letter-spacing: 0.5px; margin-top: 2px; }

  .contact-list { position: absolute; left: 300px; top: 22px; list-style: none; font-size: 8px; line-height: 9px; color: var(--ink); white-space: nowrap; }
  .contact-list__key { display: inline-block; width: 10px; color: var(--brand-red); font-weight: 700; }

  .letter-body { position: absolute; left: 54px; top: 132px; width: 356px; font-size: 9px; line-height: 10.8px; color: var(--ink); }
  .letter-body p { margin-bottom: 11px; }
  .letter-body .salutation { margin-bottom: 11px; }
  .letter-body .salutation strong { font-weight: 700; }

  .signature { position: absolute; left: 54px; top: 440px; width: 108px; height: 24px; background: var(--signature-tone); border-radius: 2px; }
  .signer { position: absolute; left: 54px; top: 477px; font-family: "Lato", sans-serif; line-height: 1.15; }
  .signer__name { font-size: 10.8px; color: var(--ink); }
  .signer__name strong { font-weight: 700; }
  .signer__role { font-size: 7px; font-weight: 700; color: var(--brand-red); letter-spacing: 0.6px; text-transform: uppercase; }

  .footer-text { position: absolute; right: 50px; bottom: 12px; text-align: right; color: #fff; font-family: "Lato", sans-serif; line-height: 1.35; }
  .footer-text__tagline { font-size: 10px; letter-spacing: 0.6px; }
  .footer-text__address { font-size: 6.6px; letter-spacing: 0.4px; }
</style>
</head>
<body>

  <section class="sheet sheet--cover" aria-label="Letterhead cover page">
    <div class="top-band">
      <div class="top-band__red"></div>
      <div class="top-band__black"></div>
    </div>
    <div class="wordmark wordmark--large">
      <span class="wordmark__name">VTM</span>
      <span class="wordmark__sub">Tech Group</span>
    </div>
    <svg class="footer-wave" viewBox="0 0 462 72" preserveAspectRatio="none" aria-hidden="true">
      <path d="M0 4 C 120 0, 230 26, 340 24 C 395 23, 435 17, 462 12 L462 72 L0 72 Z" fill="var(--brand-red)"/>
      <path d="M0 15 C 120 11, 230 36, 340 34 C 395 33, 435 27, 462 22 L462 72 L0 72 Z" fill="var(--paper)"/>
      <path d="M0 18 C 120 14, 230 39, 340 37 C 395 36, 435 30, 462 25 L462 72 L0 72 Z" fill="var(--brand-black)"/>
    </svg>
  </section>

  <section class="sheet sheet--letter" aria-label="Letterhead letter page">
    <div class="wordmark wordmark--small">
      <span class="wordmark__name">VTM</span>
      <span class="wordmark__sub">Tech Group</span>
    </div>
    <ul class="contact-list">
      <li><span class="contact-list__key">O</span>: 555.214.3380</li>
      <li><span class="contact-list__key">F</span>: 555.214.3391</li>
      <li><span class="contact-list__key">C</span>: 555.870.1127</li>
      <li><span class="contact-list__key">E</span>: dana@vtmtechgroup.com</li>
      <li><span class="contact-list__key">W</span>: www.vtmtechgroup.com</li>
    </ul>

    <div class="letter-body">
      <p class="salutation">Lorem<br><strong>ipsum dolor sit amet,</strong></p>
      <p>consectetur adipiscing elit. Duis facilisis elementum dui, bibendum pulvinar nulla malesuada quis. Curabitur ut leo quam. Pellentesque laoreet metus risus, non fermentum arcu malesuada vitae. Vestibulum dui libero, vestibulum non quam sit amet, auctor lobortis tortor. Integer blandit enim vitae adipiscing adipiscing. Vivamus metus lacus, porta at aliquam sit amet,</p>
      <p>&nbsp;pretium ut eros. Curabitur a dui interdum, elementum urna ut, venenatis erat. Fusce feugiat odio sed dui rhoncus auctor. Aenean posuere, odio ut facilisis tempus, nunc mauris convallis lacus, eget vulputate enim purus ac odio. Donec blandit et ipsum a aliquet. Mauris semper diam in velit vestibulum, sit amet molestie purus convallis. Duis pulvinar porttitor magna in malesuada.</p>
      <p>Nullam auctor neque orci, nec ornare odio auctor et. Phasellus eu sapien nec nibh lobortis commodo. Donec nec commodo nibh. Sed nec nulla et magna fermentum suscipit. Nam ligula nunc, facilisis iaculis venenatis eget,</p>
      <p>gravida consectetur odio. Donec in leo ac felis vestibulum feugiat. In at orci id justo adipiscing vehicula. Sed tortor purus, pellentesque vel lobortis nec, tincidunt vitae mi. Duis pellentesque augue vitae pharetra euismod.</p>
      <p>Duis vulputate, libero nec vehicula pretium, mi nisi tristique mauris, ac porttitor diam metus at ante. Pellentesque magna arcu, viverra ac lacinia nec, pharetra id est. Maecenas ullamcorper mattis tellus, et dapibus arcu sagittis malesuada.</p>
    </div>

    <div class="signature" role="img" aria-label="Handwritten signature of Dana Whitfield"></div>
    <div class="signer">
      <div class="signer__name">Dana <strong>Whitfield</strong></div>
      <div class="signer__role">President</div>
    </div>

    <svg class="footer-wave" viewBox="0 0 462 72" preserveAspectRatio="none" aria-hidden="true">
      <path d="M0 4 C 120 0, 230 26, 340 24 C 395 23, 435 17, 462 12 L462 72 L0 72 Z" fill="var(--brand-red)"/>
      <path d="M0 15 C 120 11, 230 36, 340 34 C 395 33, 435 27, 462 22 L462 72 L0 72 Z" fill="var(--paper)"/>
      <path d="M0 18 C 120 14, 230 39, 340 37 C 395 36, 435 30, 462 25 L462 72 L0 72 Z" fill="var(--brand-black)"/>
    </svg>
    <div class="footer-text">
      <div class="footer-text__tagline">Woman Owned Small Business</div>
      <div class="footer-text__address">2480 Meadow Crest Ave, Suite 210, Fairview, VA 22031</div>
    </div>
  </section>

</body>
</html>
```